Medical Internet Marketing Company Needs a Site!

We need a new, fresh website for our search engine optimization and social media marketing company. We specialize in helping medical practices, doctors, physicians, and hospitals with their online presence and web ranking. The site should lean towards being suited for these audiences.

We have several examples of website that we like as well as things that we like about them.

Here are sites that we enjoy.

www.brightwavelab.com

It's a good design for the site all around. The videos, buttons, and images are all excellent. They did a fine job.

- We really like their "contact us" side bar and want to include one like it on the secondary pages.

www.corvantis.net

- We don't like the "thickness" of the top navigation bar.
- We like the page colors, easy navigation, and big call to action phone number in the top right corner.

http://www.teluvo.com/

Out of all the examples provided, Teluvo is our favorite and closest look and style to what we are looking for.

- We really like the openness of the design, such as space between the text and background.

- We want a price page in a style very similar to their pricing page with the services listed and check-marks, etc. although we intend to have multiple service package columns much like Corvantis's SEO pricing page.

- The way the video fits into the home page header is very organized, simple, and attention grabbing. We intend to place a slider with videos here.

- We need a page design that will allow for an image slider like Teluvo's Features page.

Here's a great example of a medical internet marketing website: http://www.dermaplex.com/

Target Market(s)

Our target market is doctors, typically male and typically 40-45 years old. I

Industry/Entity Type

Marketing

Requirements
Must have
• The homepage should have a slider in the video. Interior pages should have a video in the very top similar to how they do it on www.brightwavelab.com

The top navigation tabs needed are:
- Home
- Solutions
- Resources
- About
- Why Quelvo
- Contact

The sidebar should have a GREAT call to action in it on interior pages.

There should be one interior page that is similar to this - http://www.teluvo.com/pricing/

There needs to be a page with multiple boxes that take up a row of the web page's body. This page will house all the case studies similar to brightwave lab's: http://www.brightwavelab.com/success-stories/case-studies/ The one exception is we want the case studies to be inside of "boxes" instead of between horizontal lines like brightwave lab's.
Nice to have
• Color, professional, and clean. GREAT use of calls to actions.

```html
<!DOCTYPE html>
<html lang="en">
<head>
<meta charset="utf-8">
<title>Quelvo — Medical Internet Marketing</title>
<link rel="stylesheet" href="https://fonts.googleapis.com/css2?family=Montserrat:wght@400;500;600;700&display=swap">
<style>
  :root{
    --teal:#4dbd9f;
    --teal-dark:#1ea47b;
    --teal-deep:#2f9c80;
    --orange:#d98a2a;
    --gold:#e0a020;
    --tab:#f6c58a;
    --ink:#333;
    --body:#555;
    --muted:#9a9a9a;
    --sky:#86d6ef;
    --rule:#dcdcdc;
  }
  *{margin:0;padding:0;box-sizing:border-box}
  html,body{width:1200px;height:1059px;overflow:hidden;background:#fff}
  body{position:relative;font-family:"Montserrat",sans-serif;color:var(--ink)}
  .abs{position:absolute}

  .brand{left:56px;top:30px;display:flex;align-items:center;gap:18px}
  .brand-mark{width:48px;height:48px;background:var(--teal)}
  .brand-name{font-size:56px;font-weight:400;letter-spacing:10px;color:#9a9a9a;line-height:1}

  .top-tabs{left:849px;top:0;width:304px;height:41px;background:var(--tab);border-radius:0 0 10px 10px;display:flex;align-items:center;justify-content:center;font-size:15px;font-weight:600;color:#3a2a1a}
  .top-tabs span{padding:0 20px}
  .top-tabs span+span{border-left:1px solid #d9893a}
  .phone{right:47px;top:50px;font-size:33px;font-weight:400;color:#333;white-space:nowrap}

  .main-nav{left:0;top:127px;width:1200px;height:55px;background:var(--teal);border-top:3px solid #9fe0cc;display:flex;justify-content:center}
  .main-nav a{display:block;height:52px;line-height:52px;padding:0 10px;margin:0 22px;color:#fff;font-size:20px;text-decoration:none;font-weight:500}
  .main-nav a.active{background:var(--teal-dark)}

  .video{left:59px;top:207px;width:522px;height:339px;border:4px solid var(--teal);border-radius:10px;background:linear-gradient(135deg,#3e3e3e,#222 60%,#2c2c2c)}
  .hero-title{left:614px;top:218px;font-size:31px;font-weight:400;color:var(--orange);white-space:nowrap;line-height:1.2}
  .bullets{left:655px;top:290px;width:500px;list-style:none}
  .bullets li{position:relative;padding-left:26px;font-size:16px;line-height:19px;color:var(--muted);margin-bottom:15px}
  .bullets li::before{content:"";position:absolute;left:0;top:3px;border-left:10px solid #888;border-top:6px solid transparent;border-bottom:6px solid transparent}
  .know-more{left:914px;top:493px;width:215px;height:49px;background:var(--sky);border:3px solid #bfe9f6;border-radius:8px;font-size:24px;color:#1f4f60;text-align:center;line-height:43px}

  .lower{left:0;top:588px;width:1200px;height:359px;background:#f7f7f7;border-top:1px solid #ddd}
  .welcome-title{left:40px;top:602px;width:793px;font-size:30px;font-weight:600;color:var(--gold);padding-bottom:10px;border-bottom:1px solid var(--rule)}
  .welcome-text{left:45px;top:660px;width:785px}
  .welcome-text p{font-size:14.5px;line-height:20px;color:var(--body);margin-bottom:20px}

  .sidebar{left:870px;top:589px;width:330px;height:358px;background:linear-gradient(90deg,#ececec,#f4f4f4)}
  .sidebar h3{position:absolute;left:0;width:340px;top:22px;text-align:center;font-size:22px;font-weight:600;color:var(--gold)}
  .links{position:absolute;left:51px;top:52px;width:244px;list-style:none}
  .links>li{border-bottom:1px solid var(--rule);padding:9px 32px 8px 0;text-align:right;position:relative;font-size:17px;font-weight:600;color:#444}
  .links>li::after{content:"";position:absolute;right:6px;top:10px;width:18px;height:18px;border-radius:50%;background:#dcdcdc}
  .links .sub{font-size:15px;font-weight:400;color:#444;line-height:19px;padding-top:3px}

  .footer{left:0;top:947px;width:1200px;height:92px;background:var(--teal)}
  .footer-name{left:33px;top:954px;font-size:56px;font-weight:700;letter-spacing:8px;color:#111;line-height:1}
  .rights{left:96px;top:1015px;font-size:14px;letter-spacing:2px;color:#fff}
  .newsletter{left:827px;top:961px;width:338px;height:37px;border:2px solid var(--teal-deep);border-radius:7px;background:#45b496;font-size:15px;font-weight:600;color:#8ee0c6;line-height:33px;padding-left:10px;white-space:nowrap}
  .newsletter svg{position:absolute;right:8px;top:6px}
  .footer-links{right:37px;top:1013px;font-size:13px;color:#fff;white-space:nowrap}
  .footer-links span{padding:0 10px}
  .footer-links span:last-child{padding-right:0}
</style>
</head>
<body>
  <header>
    <div class="abs brand"><div class="brand-mark"></div><div class="brand-name">QUELVO</div></div>
    <div class="abs top-tabs"><span>CONTACT US</span><span>CLIENT LOGIN</span></div>
    <div class="abs phone">Call (555) 014-7720</div>
    <nav class="abs main-nav">
      <a class="active">HOME</a><a>SOLUTIONS</a><a>RESOURCES</a><a>ABOUT</a><a>WHY QUELVO</a>
    </nav>
  </header>

  <section class="hero">
    <div class="abs video" role="img" aria-label="Video still: SEO lettering on a chalkboard with a presenter holding a laptop">
      <svg class="abs" style="left:202px;top:110px" width="112" height="112" viewBox="0 0 112 112">
        <circle cx="56" cy="56" r="54" fill="#4fd0a8" stroke="#2a8c70" stroke-width="3"/>
        <path d="M42 30 L80 56 L42 82 Z" fill="#1c5a47"/>
      </svg>
    </div>
    <h1 class="abs hero-title">LOREM IPSUM DOLOR SIT AME</h1>
    <ul class="abs bullets">
      <li>LOREM IPSUM DOLOR SIT AME LOREM IPSUM DOLOR SIT AMELOREM IPSUM DOLOR SIT AME</li>
      <li>LOREM IPSUM DOLOR SIT AMELOREM IPSUM DOLOR</li>
      <li>LOREM IPSUM DOLOR SIT AMELOREM IPSUM DOLOR SIT AMELOREM IPSUM DOLOR SIT AME</li>
      <li>LOREM IPSUM DOLOR SIT AME LOREM IPSUM DOLOR SIT AME</li>
    </ul>
    <div class="abs know-more">KNOW MORE</div>
  </section>

  <section>
    <div class="abs lower"></div>
    <h2 class="abs welcome-title">WELCOME TO OUR SITE</h2>
    <div class="abs welcome-text">
      <p>QUELVO is a national, medical Internet-marketing group. We empower doctors nationwide by building their practices with highly specialized engagement strategies designed to bring in real patients.</p>
      <p>The Quelvo logo is a readily identifiable symbol visually representing the organization, its attributes and its constituencies. Quelvo employees must adhere to the use of the logo, and its own standards for use of its logo, in order to maintain a single-family identity and promote the brand.</p>
      <p>Through use of a uniform set of standards, the departments and programs within Quelvo can enhance the reputation of one another and promote the overall organizational image.</p>
      <p>As the Quelvo logo achieves more prominent visibility locally, regionally, nationally and internationally In order to ensure proper use of the Quelvo logo approved typography, preferred paper stock, colors and placements, Norvel Studio has created the following graphic standards manual specifically for Quelvo.</p>
    </div>
    <aside class="abs sidebar">
      <h3>QUICK LINKS</h3>
      <ul class="links">
        <li>SOLUTIONS<div class="sub">Lorem ipsum dolor<br>Lorem ipsum dolor<br>Lorem ipsum dolor</div></li>
        <li>RESOURCES</li>
        <li>ABOUT US</li>
        <li>WHY QUELVO</li>
        <li>CONTACT US</li>
      </ul>
    </aside>
  </section>

  <footer>
    <div class="abs footer"></div>
    <div class="abs footer-name">QUELVO</div>
    <div class="abs rights">ALL RIGHTS RESERVED@QUELVO.COM</div>
    <div class="abs newsletter">SUBSCRIBE TO OUR NEWSLETTER
      <svg width="20" height="22" viewBox="0 0 20 22"><path d="M3 1 L18 11 L3 21 Z" fill="#8ee0c6"/></svg>
    </div>
    <div class="abs footer-links"><span>Home</span>|<span>Solutions</span>|<span>About us</span>|<span>Privacy policy</span></div>
  </footer>
</body>
</html>
```